Driftwood - CD cover for a love song for my wife

I have written a love song for my wife and had it recorded by a profesional artist. The song is called 'Driftwood' and I would like artwork for a single cardboard style cover. I am going to get the disc professionally copied (minimum) and I wantthe finished thing to look like it came from a shop. So I need a prfessional to do the design for me. The back needs to include the artist's bio and his picture, the lyrics and an little note from me - all attached together with the song itself which might give a bit of inspiration.

Target Market(s)

Female

Colors

Designer to choose colors to be used in the design.

Requirements
Nice to have
• Pop art theme with a man in a suit and woman with glasses

```html
<!DOCTYPE html>
<html lang="en">
<head>
<meta charset="utf-8">
<title>Driftwood – Single Cover Spread</title>
<link href="https://fonts.googleapis.com/css2?family=Alex+Brush&family=Roboto:wght@400;500&family=Roboto+Condensed:ital,wght@0,300;0,400;1,700&display=swap" rel="stylesheet">
<style>
  :root {
    --page-bg: #e6e7e9;
    --brick-dark: #6b3a2c;
    --brick-mid: #a0583f;
    --brick-light: #c98466;
    --jacket: #4a4a4c;
    --shirt: #4a1a22;
    --skin-warm: #d9a48a;
    --couple-plum: #6e2f4f;
    --couple-rose: #b8667a;
    --couple-glow: #fbeedd;
    --cream-text: #fff3e6;
    --white-text: #ffffff;
    --ink-dark: #1e0f14;
  }
  * { margin: 0; padding: 0; box-sizing: border-box; }
  html, body { width: 1200px; height: 1200px; overflow: hidden; }
  body {
    background: var(--page-bg);
    font-family: "Roboto", sans-serif;
    position: relative;
  }
  .cover-spread {
    position: absolute;
    left: 30px;
    top: 315px;
    width: 1140px;
    height: 570px;
    display: flex;
    box-shadow: 0 18px 30px rgba(0,0,0,0.28);
  }
  .panel {
    position: relative;
    width: 570px;
    height: 570px;
    overflow: hidden;
  }

  /* Artist panel */
  .artist-photo {
    position: absolute; inset: 0;
    background:
      radial-gradient(ellipse 38% 55% at 78% 38%, var(--skin-warm) 0%, rgba(217,164,138,0) 70%),
      linear-gradient(160deg, transparent 55%, var(--jacket) 56%, var(--jacket) 72%, var(--shirt) 73%),
      linear-gradient(180deg, var(--brick-mid) 0%, var(--brick-light) 35%, var(--brick-mid) 60%, var(--brick-dark) 100%);
  }
  .artist-title {
    position: absolute;
    left: 26px; top: 190px;
    font-family: "Alex Brush", cursive;
    font-size: 82px;
    line-height: 1;
    color: var(--cream-text);
    transform: rotate(-11deg);
    transform-origin: left center;
    white-space: nowrap;
  }
  .artist-name {
    position: absolute;
    left: 48px; top: 313px;
    font-family: "Roboto", sans-serif;
    font-weight: 500;
    font-size: 27px;
    line-height: 32px;
    color: var(--white-text);
  }
  .artist-bio {
    position: absolute;
    left: 48px; top: 360px;
    width: 272px;
    font-size: 12.2px;
    line-height: 15.5px;
    color: var(--white-text);
  }

  /* Lyrics panel */
  .couple-photo {
    position: absolute; inset: 0;
    background:
      radial-gradient(ellipse 45% 45% at 60% 45%, var(--couple-glow) 0%, rgba(251,238,221,0) 75%),
      linear-gradient(135deg, var(--couple-plum) 0%, var(--couple-rose) 45%, #e9b7a2 70%, var(--couple-glow) 100%);
  }
  .lyrics {
    position: absolute;
    left: 40px; top: 124px;
    font-family: "Roboto Condensed", sans-serif;
    font-weight: 300;
    font-size: 12.4px;
    line-height: 15.45px;
    color: var(--white-text);
    list-style: none;
  }
  .lyrics-credit {
    position: absolute;
    left: 40px; top: 495px;
    font-family: "Roboto Condensed", sans-serif;
    font-weight: 300;
    font-size: 12.4px;
    line-height: 15.5px;
    color: var(--white-text);
  }
  .lyrics-credit strong { font-weight: 700; font-style: italic; display: block; }
  .song-title {
    position: absolute;
    left: 256px; top: 318px;
    font-family: "Alex Brush", cursive;
    font-size: 78px;
    line-height: 1;
    color: var(--ink-dark);
    transform: rotate(-10deg);
    transform-origin: left center;
    white-space: nowrap;
  }
  .dedication {
    position: absolute;
    left: 424px; top: 402px;
    font-family: "Roboto Condensed", sans-serif;
    font-style: italic;
    font-weight: 700;
    color: var(--ink-dark);
  }
  .dedication h2 { font-size: 18px; line-height: 22px; font-weight: 700; }
  .dedication p { font-size: 12.2px; line-height: 15.5px; }
</style>
</head>
<body>
  <main class="cover-spread">
    <section class="panel panel-artist">
      <div class="artist-photo" role="img" aria-label="Portrait photo of the singer in profile against a blurred brick wall"></div>
      <div class="artist-title">Driftwood</div>
      <h1 class="artist-name">Sam</h1>
      <p class="artist-bio">"Growing up in the small city of Ashbury Sam Hartwell decided to travel further a field to further his music career and has performed all over the UK and Europe. In 2015 he started to work online as a session musician, writing and playing on hundreds of other musicians tracks. His acoustic covers on Tunewave have amassed millions of plays and he continues to work on both his own and others music to this day."</p>
    </section>

    <section class="panel panel-lyrics">
      <div class="couple-photo" role="img" aria-label="Warm backlit photo of a couple about to kiss"></div>
      <ul class="lyrics">
        <li>Love</li>
        <li>Its what I am to you</li>
        <li>And you are to me</li>
        <li>We walk through life hand-in-hand you and me</li>
        <li>Your strength holds me up and sets me free</li>
        <li>Its what I am to you</li>
        <li>And you are to me</li>
        <li>Your love is everything can't you see?</li>
        <li>Your kindness gives me hope and keeps me sane</li>
        <li>You're the only one who can ease my pain</li>
        <li>Its what I am to you</li>
        <li>And you are to me</li>
        <li>Your love is everything can't you see?</li>
        <li>You are my world my life and my friend</li>
        <li>I'll be here for you until the very end</li>
        <li>Its what I am to you</li>
        <li>And you are to me</li>
        <li>Your love is everything can't you see?</li>
        <li>With all my heart I thank you for your love</li>
        <li>I give mine in return though I now it's not enough</li>
        <li>Its what I am to you</li>
        <li>And you are to me</li>
        <li>Your love is everything can't you see?</li>
      </ul>
      <p class="lyrics-credit"><strong>Lyrics by</strong>Owen Marsh for Clara Marsh</p>
      <div class="song-title">Driftwood</div>
      <div class="dedication">
        <h2>Dear Clara</h2>
        <p>This is from me to you</p>
        <p>All my love</p>
        <p>Owen</p>
      </div>
    </section>
  </main>
</body>
</html>
```